Hearth of the Heron: Half-Page Magazine Ad

advertisement in a travel magazine for a casual/fine dining restaurant in the heart of Whitehorse, Yukon
Needs to say that it is located in the Stonereach Hotel, 247 Larch Avenue.

Northern inspired cuisine
hearthoftheheron-example.ca

Don't need to use all the pictures

Dimensions: ad is a half-page, dimensions are 7.25" x 4.8".

Target Market(s)

Upscale dining, corporate travellers

Industry/Entity Type

Restaurant

Colors
0054AA
0677BA
7BADD7
CADEEF
E8F1F8
0094D4
00A9DD
6FCCEA
C7EBF8
E9F6FB
00AB8E
00BBA5
67D7C9
C6EFE9
E9F9F6

Requirements
Must have
• Restaurant logo
Nice to have
• Simple, clean design with upscale feel

```html
<!DOCTYPE html>
<html lang="en">
<head>
<meta charset="utf-8">
<title>Hearth of the Heron – Magazine Ad</title>
<link rel="stylesheet" href="https://fonts.googleapis.com/css2?family=Montserrat:wght@400;500;600;700&family=Kaushan+Script&display=swap">
<style>
:root{
  --stage:#b7b7b7;
  --ink:#231f20;
  --paper:#ffffff;
  --frame:#f4f4f4;
  --text-light:#ffffff;
  --text-dark:#231f20;
}
*{margin:0;padding:0;box-sizing:border-box}
html,body{width:1200px;height:2298px;overflow:hidden;background:var(--stage)}
.ad{
  position:absolute;left:55px;top:377px;width:1090px;height:1543px;
  background:var(--ink);overflow:hidden;
  box-shadow:0 6px 14px rgba(0,0,0,.35);
  font-family:'Montserrat',sans-serif;
}
.photo-frame{position:absolute;left:44px;top:47px;width:1002px;height:906px;background:var(--frame)}
.tile{position:absolute}
.tile-board{left:3px;top:3px;width:293px;height:335px;
  background:linear-gradient(135deg,#6f5a4a 0%,#b8784f 35%,#d9b864 60%,#4d5a33 100%)}
.tile-logo{left:299px;top:3px;width:403px;height:335px;background:var(--paper);
  display:flex;align-items:center;justify-content:center;gap:22px}
.logo-mark{width:46px;height:46px;border-radius:50%;background:var(--ink)}
.logo-name{font-family:'Montserrat',sans-serif;font-weight:700;font-size:40px;line-height:1.05;color:var(--ink);text-transform:uppercase;letter-spacing:1px}
.tile-salad{left:705px;top:3px;width:294px;height:335px;
  background:linear-gradient(160deg,#e58a5c 0%,#d8a04a 35%,#7d8a3c 65%,#c7c0c8 100%)}
.tile-pasta{left:3px;top:342px;width:996px;height:561px;
  background:radial-gradient(ellipse at 42% 55%,#e0782f 0%,#c35a24 35%,#a3a3a3 62%,#8fa9c9 85%,#6f8fbf 100%)}
.headline{position:absolute;left:0;right:0;top:975px;text-align:center;
  font-family:'Kaushan Script',cursive;font-size:92px;color:var(--text-light);line-height:1}
.pitch{position:absolute;left:0;right:0;top:1124px;text-align:center;
  font-size:27.5px;line-height:34px;color:var(--text-light);font-weight:400}
.features{position:absolute;left:0;right:0;top:1222px;height:80px}
.feature{position:absolute;top:0;display:flex;gap:14px;color:var(--text-light);
  font-weight:600;font-size:28px;line-height:33px}
.feature svg{flex:none;margin-top:6px}
.feature-patio{left:118px}
.feature-cuisine{left:622px}
.divider{position:absolute;left:544px;top:8px;width:2px;height:72px;background:var(--text-light)}
.location-band{position:absolute;left:0;right:0;top:1360px;bottom:0;background:var(--paper)}
.location-tag{position:absolute;left:369px;top:1332px;width:354px;height:53px}
.location-tag svg{position:absolute;inset:0}
.location-tag span{position:relative;display:block;text-align:center;line-height:53px;
  font-weight:600;font-size:27px;color:var(--text-light);letter-spacing:.5px}
.address{position:absolute;left:0;right:0;top:1408px;text-align:center;
  font-weight:700;font-size:36px;color:var(--text-dark)}
.website{position:absolute;left:0;right:0;top:1472px;text-align:center;
  font-weight:500;font-size:22px;letter-spacing:4.5px;color:var(--text-dark)}
</style>
</head>
<body>
<main class="ad">
  <div class="photo-frame">
    <div class="tile tile-board" role="img" aria-label="Charcuterie board with cured meats, cheeses, crackers and pickles"></div>
    <div class="tile tile-logo">
      <span class="logo-mark"></span>
      <span class="logo-name">Hearth<br>of the<br>Heron</span>
    </div>
    <div class="tile tile-salad" role="img" aria-label="Crab claw with squash soup and a citrus salad"></div>
    <div class="tile tile-pasta" role="img" aria-label="Bowl of pappardelle in red sauce topped with shaved parmesan and microgreens"></div>
  </div>

  <h1 class="headline">Hearth of the Heron</h1>
  <p class="pitch">Elegant comfort food that is upscale but simple. Paired with an<br>impressive wine selection and a modern spin on classic cocktails.</p>

  <div class="features">
    <div class="feature feature-patio">
      <svg width="30" height="28" viewBox="0 0 30 28" aria-hidden="true"><circle cx="13" cy="15" r="11" fill="none" stroke="#fff" stroke-width="3"/><path d="M7 14l6 7L28 3" fill="none" stroke="#fff" stroke-width="3.5" stroke-linecap="round" stroke-linejoin="round"/></svg>
      <span>Open evenings with<br>a summer patio.</span>
    </div>
    <div class="divider"></div>
    <div class="feature feature-cuisine">
      <svg width="30" height="28" viewBox="0 0 30 28" aria-hidden="true"><circle cx="13" cy="15" r="11" fill="none" stroke="#fff" stroke-width="3"/><path d="M7 14l6 7L28 3" fill="none" stroke="#fff" stroke-width="3.5" stroke-linecap="round" stroke-linejoin="round"/></svg>
      <span>Northern inspired<br>cuisine</span>
    </div>
  </div>

  <div class="location-band"></div>
  <div class="location-tag">
    <svg viewBox="0 0 354 53" preserveAspectRatio="none" aria-hidden="true"><polygon points="22,0 354,0 332,53 0,53" fill="#231f20" stroke="#fff" stroke-width="2"/></svg>
    <span>LOCATED IN THE</span>
  </div>
  <p class="address">Stonereach Hotel, 247 Larch Avenue.</p>
  <p class="website">www.hearthoftheheron-example.ca</p>
</main>
</body>
</html>
```